Door Hanger Design for Electricians Serving Homes

I would like our logo incorporated into the door hanger. We would like a place for a tear off section on the bottom of the hanger with our contact information: K&T Electric - (555) 318-6470 - www.kandtelectric.example - info@kandtelectric.example.
Door Hanger Script
Front Side of the Door Hanger:
[Company Logo]
Need a Reliable Electrician?
Your Local Electrical Expert is Just Around the Corner!
• Quick Response Times
• Affordable Rates
• Quality Workmanship
• Fully Licensed & Insured
• Special Offer:
• 10% OFF Your First Service Call!
Back Side of the Door Hanger:
Don't Let Electrical Issues Keep You in the Dark!
From flickering lights to complete system upgrades, we've got all your
residential electrical needs covered. Our services include:
• Electrical Repairs & Troubleshooting
• Lighting Installation & Upgrades
• Safety Inspections & Code Compliance
• Energy-Efficient Solutions
• 24/7 Emergency Services
• Why Choose Us?
• Friendly, Local Service
• Over 30 Years of Experience
• Satisfaction Guaranteed
• Upfront Pricing
Call Us Today: [Your Phone Number]
Visit Our Website: [Your Website]
Book Your Appointment Now and Claim Your 10% Discount!
Offer valid for new customers on the first visit only. Mention this door hanger when
booking.
[Your Company Name and Contact Information]
Follow Us on Social Media for More Tips and Special Offers!
[Icons for social media platforms: Chatterbook, Snapwave, Peeper, etc.]
Design Tips:
Use bold, clear fonts for easy reading.
Incorporate your brand colors and logo for instant recognition.
Include a clear call to action (CTA) on both sides.
Add a tear-off section at the bottom with your contact information for
convenience.
Use high-quality images or graphics related to electrical work to catch
the eye.
This door hanger design and copy aim to attract residential clients by
highlighting the benefits of your electrical services, special offers, and
how they can easily get in touch with you for their electrical needs.
The door knocker template will have three of the same design on front and three of the same design on the back. This template is from the print shop.

```html
<!DOCTYPE html>
<html lang="en">
<head>
<meta charset="utf-8">
<title>K&amp;T Electric Door Hanger</title>
<link rel="stylesheet" href="https://fonts.googleapis.com/css2?family=Poppins:wght@300;400;500;700;800&display=swap">
<style>
:root{
  --bg:#e8e8e8;
  --red:#d40a0a;
  --red-deep:#a80000;
  --red-soft:#c8282b;
  --ink:#111111;
  --white:#ffffff;
  --card:#f8f8f8;
  --hole:#bab6b5;
  --text:#222222;
}
*{margin:0;padding:0;box-sizing:border-box}
html,body{width:1200px;height:1200px;overflow:hidden;background:var(--bg);font-family:'Poppins',sans-serif;color:var(--text)}
.hanger{position:absolute;top:107px;width:380px;height:984px;background:var(--white);box-shadow:0 10px 30px rgba(0,0,0,.18);overflow:hidden}
.hanger--front{left:196px}
.hanger--back{left:642px}
.abs{position:absolute}
.hole{position:absolute;left:140px;top:24px;width:100px;height:100px;border-radius:50%;background:var(--hole);z-index:3}
.front-hero{position:absolute;left:0;top:0;width:380px;height:566px;background:radial-gradient(circle at 70% 30%,#c41010 0%,#a80000 55%,#8e0000 100%)}
.house-photo{position:absolute;left:0;top:340px;width:380px;height:226px;background:linear-gradient(180deg,#5a5f7a 0%,#4a4f66 45%,#6b4a2e 75%,#3a3a3a 100%)}
.center{width:100%;text-align:center;color:var(--white)}
.need{top:142px;font-weight:300;font-size:37px;letter-spacing:1px;line-height:1}
.big{font-weight:800;font-size:44px;line-height:1;letter-spacing:.5px}
.reliable{top:192px}
.electrician{top:234px}
.tagline{top:272px;font-size:19.5px;line-height:24px;font-weight:400}
.card{position:absolute;background:var(--card);box-shadow:0 1px 4px rgba(0,0,0,.18);text-align:center}
.card svg{position:absolute;left:50%;transform:translateX(-50%)}
.card .label{position:absolute;left:0;width:100%;font-size:10px;line-height:10px;color:var(--text)}
.brand{font-family:'Poppins',sans-serif;font-weight:700;color:var(--ink);text-align:center}
.contact-bar{position:absolute;background:var(--ink);color:var(--white);font-size:10.5px;display:flex;align-items:center;justify-content:center;gap:14px}
.contact-bar span{display:flex;align-items:center;gap:4px}
.url-bar{position:absolute;background:var(--red);color:var(--white);font-size:10px;letter-spacing:1.2px;display:flex;align-items:center;justify-content:center;gap:4px}
.back-hero{position:absolute;left:0;top:0;width:380px;height:248px;background:linear-gradient(120deg,#d63a3a 0%,#c92a2a 50%,#b81f22 100%)}
.headline{top:138px;font-weight:800;font-size:20.5px;line-height:24px}
.subline{top:192px;font-size:12.3px;line-height:12.5px}
.pill{position:absolute;background:var(--ink);color:var(--white);border-radius:7px;font-size:12.5px;display:flex;align-items:center;justify-content:center}
.cta{position:absolute;left:23px;top:690px;width:331px;height:87px;background:var(--red);border-radius:9px;color:var(--white);text-align:center}
.cta .l1{position:absolute;top:6px;width:100%;font-size:18.5px;line-height:19.5px;font-weight:500}
.cta .l2{position:absolute;top:45px;width:100%;font-size:33px;line-height:36px;font-weight:800}
.offer{left:170px;top:801px;width:180px;font-size:9.5px;line-height:12px;color:var(--text)}
.follow{left:55px;top:943px;font-size:10.5px;line-height:11px;color:var(--text)}
.social{position:absolute;top:947px;width:12px;height:12px;background:var(--red)}
</style>
</head>
<body>

<!-- Front side -->
<section class="hanger hanger--front">
  <div class="front-hero" role="img" aria-label="Red-tinted photo of an electrician at work"></div>
  <div class="house-photo" role="img" aria-label="Photo of a lit two-storey suburban house at dusk"></div>
  <div class="hole"></div>

  <div class="abs center need">NEED A</div>
  <div class="abs center big reliable">RELIABLE</div>
  <div class="abs center big electrician">ELECTRICIAN</div>
  <div class="abs center tagline">Your Local Electrical Expert is<br>Just Around the Corner!</div>

  <div class="card" style="left:32px;top:583px;width:95px;height:93px">
    <svg style="top:10px" width="32" height="30" viewBox="0 0 32 30"><circle cx="19" cy="16" r="10" fill="none" stroke="#d40a0a" stroke-width="2.5"/><rect x="16" y="2" width="6" height="3" fill="#d40a0a"/><path d="M19 16 L19 10 M19 16 L23 18" stroke="#d40a0a" stroke-width="2"/><path d="M2 12h7M0 17h7M3 22h7" stroke="#d40a0a" stroke-width="2"/></svg>
    <div class="label" style="top:60px">Quick Response<br>Times</div>
  </div>
  <div class="card" style="left:141px;top:583px;width:95px;height:93px">
    <svg style="top:8px" width="32" height="32" viewBox="0 0 32 32"><rect x="3" y="12" width="26" height="18" fill="#d40a0a"/><rect x="7" y="17" width="4" height="5" fill="#fff"/><rect x="14" y="17" width="4" height="5" fill="#fff"/><rect x="21" y="17" width="4" height="5" fill="#fff"/><circle cx="16" cy="7" r="5" fill="#d40a0a"/><text x="16" y="9.5" font-size="7" fill="#fff" text-anchor="middle" font-family="Poppins,sans-serif">$</text></svg>
    <div class="label" style="top:60px">Affordable Rates</div>
  </div>
  <div class="card" style="left:252px;top:583px;width:95px;height:93px">
    <svg style="top:8px" width="32" height="32" viewBox="0 0 32 32"><circle cx="16" cy="16" r="15" fill="#d40a0a"/><circle cx="16" cy="16" r="9" fill="none" stroke="#fff" stroke-width="2"/><path d="M11.5 16l3 3 6-6" fill="none" stroke="#fff" stroke-width="2.4"/></svg>
    <div class="label" style="top:60px">Quality<br>Workmanship</div>
  </div>
  <div class="card" style="left:32px;top:686px;width:95px;height:93px">
    <svg style="top:7px" width="28" height="32" viewBox="0 0 28 32"><path d="M3 1h16l6 6v24H3z" fill="#d40a0a"/><path d="M7 10h12M7 15h12M7 20h9M7 25h6" stroke="#fff" stroke-width="2"/><circle cx="22" cy="25" r="5" fill="#fff" stroke="#d40a0a" stroke-width="2"/></svg>
    <div class="label" style="top:46px">Fully Licensed &amp;<br>Insured</div>
  </div>
  <div class="card" style="left:141px;top:686px;width:95px;height:93px">
    <svg style="top:6px" width="32" height="32" viewBox="0 0 32 32"><path d="M4 18l14-10 4 14-14 2z" fill="#d40a0a"/><circle cx="9" cy="22" r="5" fill="#d40a0a"/><path d="M24 6l3-3M26 12h4M22 3l1-3" stroke="#d40a0a" stroke-width="2"/></svg>
    <div class="label" style="top:46px">Special Offer</div>
  </div>
  <div class="card" style="left:252px;top:686px;width:95px;height:93px">
    <svg style="top:6px" width="28" height="32" viewBox="0 0 28 32"><circle cx="14" cy="10" r="7" fill="#d40a0a"/><path d="M1 31c0-9 6-13 13-13s13 4 13 13z" fill="#d40a0a"/><path d="M6 10a8 8 0 0 1 16 0" fill="none" stroke="#111" stroke-width="2"/></svg>
    <div class="label" style="top:46px">10% OFF Your First<br>Service Call!</div>
  </div>

  <div class="abs brand" style="left:0;top:818px;width:380px;font-size:26px;line-height:30px">K&amp;T</div>
  <div class="abs brand" style="left:0;top:848px;width:380px;font-size:12px;line-height:14px">Electric, LLC</div>

  <div class="contact-bar" style="left:32px;top:904px;width:317px;height:44px;padding-bottom:6px">
    <span><svg width="9" height="9" viewBox="0 0 10 10"><path d="M2 1l2 2-1 1.5a6 6 0 0 0 2.5 2.5L7 6l2 2-1.5 1.5C4 9 1 6 .5 2.5z" fill="#d40a0a"/></svg>(555) 318-6470</span>
    <span><svg width="9" height="7" viewBox="0 0 10 7"><rect width="10" height="7" fill="#d40a0a"/><path d="M0 0l5 4 5-4" stroke="#fff" fill="none"/></svg>info@kandtelectric.example</span>
  </div>
  <div class="url-bar" style="left:109px;top:940px;width:163px;height:18px;font-size:9px;letter-spacing:.6px">
    <svg width="7" height="7" viewBox="0 0 10 10"><circle cx="5" cy="5" r="4.2" fill="none" stroke="#fff" stroke-width="1.2"/></svg>www.kandtelectric.example
  </div>
</section>

<!-- Back side -->
<section class="hanger hanger--back">
  <div class="back-hero" role="img" aria-label="Red-tinted photo of an electrician checking a ceiling light fitting"></div>
  <div class="hole"></div>

  <div class="abs center headline">Don't Let Electrical Issues<br>Keep You in the Dark!</div>
  <div class="abs center subline">From flickering lights to complete system upgrades,<br>we've got all your residential electrical needs covered.</div>

  <div class="pill" style="left:113px;top:238px;width:143px;height:20px">Our services</div>

  <div class="card" style="left:28px;top:272px;width:96px;height:85px">
    <svg style="top:9px" width="24" height="24" viewBox="0 0 24 24"><circle cx="12" cy="12" r="8" fill="none" stroke="#d40a0a" stroke-width="4" stroke-dasharray="4 2.3"/><circle cx="12" cy="12" r="4" fill="none" stroke="#d40a0a" stroke-width="2"/></svg>
    <div class="label" style="top:43px">Electrical<br>Repairs &amp;<br>Troubleshooting</div>
  </div>
  <div class="card" style="left:138px;top:272px;width:96px;height:85px">
    <svg style="top:8px" width="16" height="26" viewBox="0 0 16 26"><path d="M10 0L1 15h6l-3 11 11-16H9z" fill="#d40a0a"/></svg>
    <div class="label" style="top:43px">Lighting<br>Installation<br>&amp; Upgrades</div>
  </div>
  <div class="card" style="left:248px;top:272px;width:96px;height:85px">
    <svg style="top:8px" width="26" height="26" viewBox="0 0 26 26"><circle cx="13" cy="13" r="11" fill="none" stroke="#d40a0a" stroke-width="2.5" stroke-dasharray="26 4"/><path d="M14 5l-6 9h4l-2 7 6-10h-4z" fill="#d40a0a"/></svg>
    <div class="label" style="top:43px">Energy-Efficient<br>Solutions</div>
  </div>
  <div class="card" style="left:82px;top:367px;width:96px;height:86px">
    <svg style="top:10px" width="24" height="16" viewBox="0 0 24 16"><path d="M2 13a10 10 0 0 1 20 0z" fill="#d40a0a"/><rect x="0" y="13" width="24" height="3" fill="#d40a0a"/><path d="M9 4v9M15 4v9" stroke="#fff" stroke-width="1.2"/></svg>
    <div class="label" style="top:39px">Safety<br>Inspections<br>&amp; Code<br>Compliance</div>
  </div>
  <div class="card" style="left:191px;top:367px;width:96px;height:86px">
    <svg style="top:10px" width="26" height="26" viewBox="0 0 26 26"><circle cx="13" cy="13" r="11.5" fill="none" stroke="#d40a0a" stroke-width="2"/><path d="M7 7l3 3-1.5 2a8 8 0 0 0 4.5 4.5l2-1.5 3 3-2 2C10 19 5 14 5 9z" fill="#d40a0a"/><text x="18" y="10" font-size="5.5" fill="#d40a0a" text-anchor="middle" font-family="Poppins,sans-serif">24</text></svg>
    <div class="label" style="top:43px">24/7 Emergency<br>Services</div>
  </div>

  <div class="pill" style="left:123px;top:466px;width:143px;height:20px">Why Choose Us?</div>

  <div class="card" style="left:83px;top:494px;width:96px;height:86px">
    <svg style="top:12px" width="24" height="20" viewBox="0 0 24 20"><path d="M1 6c3-5 19-5 22 0v3h-5V6H6v3H1z" fill="#d40a0a"/><rect x="3" y="9" width="18" height="11" rx="2" fill="#d40a0a"/><circle cx="12" cy="14.5" r="3" fill="#fff"/></svg>
    <div class="label" style="top:49px">Friendly, Local<br>Service</div>
  </div>
  <div class="card" style="left:193px;top:494px;width:96px;height:86px">
    <svg style="top:12px" width="24" height="20" viewBox="0 0 24 20"><circle cx="9" cy="7" r="3" fill="#d40a0a"/><path d="M3 16a6 6 0 0 1 12 0z" fill="#d40a0a"/><circle cx="18" cy="15" r="4" fill="#d40a0a"/><path d="M16 15l1.5 1.5 2.5-3" stroke="#fff" fill="none" stroke-width="1.2"/><circle cx="4" cy="2" r="1" fill="#d40a0a"/><circle cx="9" cy="1" r="1" fill="#d40a0a"/><circle cx="14" cy="2" r="1" fill="#d40a0a"/></svg>
    <div class="label" style="top:49px">Over 30 Years<br>of Experience</div>
  </div>
  <div class="card" style="left:83px;top:589px;width:96px;height:84px">
    <svg style="top:12px" width="22" height="22" viewBox="0 0 22 22"><circle cx="11" cy="11" r="11" fill="#d40a0a"/><text x="11" y="15.5" font-size="13" fill="#fff" text-anchor="middle" font-family="Poppins,sans-serif">$</text></svg>
    <div class="label" style="top:47px">Upfront Pricing</div>
  </div>
  <div class="card" style="left:193px;top:589px;width:96px;height:84px">
    <svg style="top:12px" width="24" height="22" viewBox="0 0 24 22"><circle cx="14" cy="7" r="6" fill="#d40a0a"/><path d="M11 7l2 2 4-4" stroke="#fff" fill="none" stroke-width="1.5"/><path d="M1 15h5l6 2h8v3H8l-7-1z" fill="#d40a0a"/></svg>
    <div class="label" style="top:47px">Satisfaction<br>Guaranteed</div>
  </div>

  <div class="cta">
    <div class="l1">Book Your Appointment<br>Now and Claim Your</div>
    <div class="l2">10% Discount!</div>
  </div>

  <div class="abs brand" style="left:40px;top:792px;width:110px;font-size:30px;line-height:38px">K&amp;T</div>
  <div class="abs brand" style="left:40px;top:836px;width:110px;font-size:12px;line-height:14px">Electric, LLC</div>
  <div class="abs offer">Offer valid for new customers on the first visit only. Mention this door hanger when booking.</div>

  <div class="contact-bar" style="left:30px;top:876px;width:317px;height:41px;font-size:12px;align-items:flex-start;padding-top:9px;gap:16px">
    <span><svg width="10" height="10" viewBox="0 0 10 10"><path d="M2 1l2 2-1 1.5a6 6 0 0 0 2.5 2.5L7 6l2 2-1.5 1.5C4 9 1 6 .5 2.5z" fill="#d40a0a"/></svg>(555) 318-6470</span>
    <span><svg width="10" height="7" viewBox="0 0 10 7"><rect width="10" height="7" fill="#d40a0a"/><path d="M0 0l5 4 5-4" stroke="#fff" fill="none"/></svg>info@kandtelectric.example</span>
  </div>
  <div class="url-bar" style="left:94px;top:909px;width:190px;height:20px;font-size:10px;letter-spacing:.8px">
    <svg width="8" height="8" viewBox="0 0 10 10"><circle cx="5" cy="5" r="4.2" fill="none" stroke="#fff" stroke-width="1.2"/></svg>www.kandtelectric.example
  </div>

  <div class="abs follow">Follow Us on Social Media for More<br>Tips and Special Offers!</div>
  <div class="social" style="left:255px" aria-label="Snapwave"></div>
  <div class="social" style="left:272px" aria-label="Chatterbook"></div>
  <div class="social" style="left:289px" aria-label="Peeper"></div>
</section>

</body>
</html>
```